Step and Repeat Backdrop for wedding reception photo booth

Would like to have a Step and Repeat Backdrop (8 foot high by 10 foot wide) that incorporates the wedding logo (attached) and the names Elena and Gavin. Background should be white, and wedding colors are burgundy and gold. Show me creativity :-) I have included some random samples.

```html
<!DOCTYPE html>
<html lang="en">
<head>
<meta charset="utf-8">
<title>Elena and Gavin – Step and Repeat Backdrop</title>
<link rel="stylesheet" href="https://fonts.googleapis.com/css2?family=Parisienne&family=Playfair+Display:wght@500&display=swap">
<style>
  :root {
    --paper: #ffffff;
    --banner: #fdfdfc;
    --gold: #d2ab67;
    --gold-deep: #b48a4a;
    --frame: #e2c99d;
  }
  * { margin: 0; padding: 0; box-sizing: border-box; }
  html, body {
    width: 1200px;
    height: 960px;
    overflow: hidden;
    background: var(--paper);
  }
  .backdrop {
    position: relative;
    width: 1200px;
    height: 960px;
    overflow: hidden;
    background: var(--paper);
  }
  .monogram-grid {
    position: absolute;
    left: 23px;
    top: 15px;
    display: grid;
    grid-template-columns: repeat(10, 103px);
    grid-auto-rows: 94px;
    column-gap: 15px;
    row-gap: 17px;
  }
  .monogram-tile {
    display: flex;
    align-items: center;
    justify-content: center;
    font-family: "Playfair Display", serif;
    font-weight: 500;
    font-size: 40px;
    letter-spacing: -1px;
    color: var(--gold-deep);
    border: 1px solid transparent;
  }
  .monogram-tile.framed {
    border-color: var(--frame);
  }
  .name-banner {
    position: absolute;
    left: 55px;
    top: 363px;
    width: 1089px;
    height: 224px;
    background: var(--banner);
  }
  .couple-names {
    position: absolute;
    left: 0;
    top: 360px;
    width: 1200px;
    text-align: center;
    font-family: "Parisienne", cursive;
    font-size: 150px;
    line-height: 1.3;
    color: var(--gold);
    white-space: nowrap;
  }
</style>
</head>
<body>
<main class="backdrop">
  <div class="monogram-grid" aria-hidden="true">
    <!-- row 1 -->
    <div class="monogram-tile">E&amp;G</div><div class="monogram-tile framed">E&amp;G</div><div class="monogram-tile">E&amp;G</div><div class="monogram-tile framed">E&amp;G</div><div class="monogram-tile">E&amp;G</div><div class="monogram-tile framed">E&amp;G</div><div class="monogram-tile">E&amp;G</div><div class="monogram-tile framed">E&amp;G</div><div class="monogram-tile">E&amp;G</div><div class="monogram-tile framed">E&amp;G</div>
    <!-- row 2 -->
    <div class="monogram-tile framed">E&amp;G</div><div class="monogram-tile">E&amp;G</div><div class="monogram-tile framed">E&amp;G</div><div class="monogram-tile">E&amp;G</div><div class="monogram-tile framed">E&amp;G</div><div class="monogram-tile">E&amp;G</div><div class="monogram-tile framed">E&amp;G</div><div class="monogram-tile">E&amp;G</div><div class="monogram-tile framed">E&amp;G</div><div class="monogram-tile">E&amp;G</div>
    <!-- row 3 -->
    <div class="monogram-tile">E&amp;G</div><div class="monogram-tile framed">E&amp;G</div><div class="monogram-tile">E&amp;G</div><div class="monogram-tile framed">E&amp;G</div><div class="monogram-tile">E&amp;G</div><div class="monogram-tile framed">E&amp;G</div><div class="monogram-tile">E&amp;G</div><div class="monogram-tile framed">E&amp;G</div><div class="monogram-tile">E&amp;G</div><div class="monogram-tile framed">E&amp;G</div>
    <!-- row 4 -->
    <div class="monogram-tile framed">E&amp;G</div><div class="monogram-tile">E&amp;G</div><div class="monogram-tile framed">E&amp;G</div><div class="monogram-tile">E&amp;G</div><div class="monogram-tile framed">E&amp;G</div><div class="monogram-tile">E&amp;G</div><div class="monogram-tile framed">E&amp;G</div><div class="monogram-tile">E&amp;G</div><div class="monogram-tile framed">E&amp;G</div><div class="monogram-tile">E&amp;G</div>
    <!-- row 5 -->
    <div class="monogram-tile">E&amp;G</div><div class="monogram-tile framed">E&amp;G</div><div class="monogram-tile">E&amp;G</div><div class="monogram-tile framed">E&amp;G</div><div class="monogram-tile">E&amp;G</div><div class="monogram-tile framed">E&amp;G</div><div class="monogram-tile">E&amp;G</div><div class="monogram-tile framed">E&amp;G</div><div class="monogram-tile">E&amp;G</div><div class="monogram-tile framed">E&amp;G</div>
    <!-- row 6 -->
    <div class="monogram-tile framed">E&amp;G</div><div class="monogram-tile">E&amp;G</div><div class="monogram-tile framed">E&amp;G</div><div class="monogram-tile">E&amp;G</div><div class="monogram-tile framed">E&amp;G</div><div class="monogram-tile">E&amp;G</div><div class="monogram-tile framed">E&amp;G</div><div class="monogram-tile">E&amp;G</div><div class="monogram-tile framed">E&amp;G</div><div class="monogram-tile">E&amp;G</div>
    <!-- row 7 -->
    <div class="monogram-tile">E&amp;G</div><div class="monogram-tile framed">E&amp;G</div><div class="monogram-tile">E&amp;G</div><div class="monogram-tile framed">E&amp;G</div><div class="monogram-tile">E&amp;G</div><div class="monogram-tile framed">E&amp;G</div><div class="monogram-tile">E&amp;G</div><div class="monogram-tile framed">E&amp;G</div><div class="monogram-tile">E&amp;G</div><div class="monogram-tile framed">E&amp;G</div>
    <!-- row 8 -->
    <div class="monogram-tile framed">E&amp;G</div><div class="monogram-tile">E&amp;G</div><div class="monogram-tile framed">E&amp;G</div><div class="monogram-tile">E&amp;G</div><div class="monogram-tile framed">E&amp;G</div><div class="monogram-tile">E&amp;G</div><div class="monogram-tile framed">E&amp;G</div><div class="monogram-tile">E&amp;G</div><div class="monogram-tile framed">E&amp;G</div><div class="monogram-tile">E&amp;G</div>
    <!-- row 9 -->
    <div class="monogram-tile">E&amp;G</div><div class="monogram-tile framed">E&amp;G</div><div class="monogram-tile">E&amp;G</div><div class="monogram-tile framed">E&amp;G</div><div class="monogram-tile">E&amp;G</div><div class="monogram-tile framed">E&amp;G</div><div class="monogram-tile">E&amp;G</div><div class="monogram-tile framed">E&amp;G</div><div class="monogram-tile">E&amp;G</div><div class="monogram-tile framed">E&amp;G</div>
  </div>

  <div class="name-banner"></div>
  <h1 class="couple-names">Elena and Gavin.</h1>
</main>
</body>
</html>
```